Brindle Hollow Jerky packaging

We are looking for a modern, upmarket packaging for our range of beef jerky. Our existing logo is attached for your reference.
We aim to have our product placed in gastro pubs, craft beer events, bottle shops and hotels. The retail package itself will be 60g net and approximately 17cm x 14cm. There will be 4 flavours (original, chilli, smoked pepper and mongolian).
We would like to see some illustration in the design to showcase the different flavours. Use of colour and/or window is optional.

```html
<!DOCTYPE html>
<html lang="en">
<head>
<meta charset="utf-8">
<title>Brindle Hollow Jerky – Packaging Range</title>
<link rel="stylesheet" href="https://fonts.googleapis.com/css2?family=Alfa+Slab+One&family=Oswald:wght@500;700&family=Roboto+Condensed:wght@400;700&display=swap">
<style>
  :root{
    --stage:#777777;
    --pouch-light:#f3f3f3;
    --pouch-mid:#d6d6d6;
    --plank-line:rgba(120,120,120,.18);
    --grain-line:rgba(140,140,140,.07);
    --ink:#2b2b2b;
    --kraft:#c9a77b;
    --kraft-dark:#a8865a;
    --jerky:#7a3b22;
    --jerky-dark:#4e2414;
    --chilli:#9b1c1f;
    --original:#e87722;
    --pepper:#5a3319;
    --mongolian:#4d6b23;
  }
  *{box-sizing:border-box;margin:0;padding:0}
  html,body{width:1200px;height:1200px;overflow:hidden;background:var(--stage)}
  .range{position:relative;width:1200px;height:1200px}
  .flavour-pair{position:absolute;width:540px;height:370px}
  .flavour-pair.chilli{left:45px;top:205px;--accent:var(--chilli)}
  .flavour-pair.original{left:640px;top:205px;--accent:var(--original)}
  .flavour-pair.pepper{left:45px;top:628px;--accent:var(--pepper)}
  .flavour-pair.mongolian{left:640px;top:628px;--accent:var(--mongolian)}

  .pouch{position:absolute;top:0;width:258px;height:362px;border-radius:10px 10px 6px 6px;overflow:hidden;
    font-family:"Roboto Condensed",sans-serif;color:var(--ink);
    background:
      repeating-linear-gradient(90deg,transparent 0 31px,var(--plank-line) 31px 32px),
      repeating-linear-gradient(90deg,transparent 0 5px,var(--grain-line) 5px 6px,transparent 6px 13px),
      linear-gradient(90deg,var(--pouch-mid),var(--pouch-light) 25%,#fbfbfb 55%,var(--pouch-light) 80%,var(--pouch-mid));
    box-shadow:0 3px 8px rgba(0,0,0,.25)}
  .pouch.back{left:0}
  .pouch.front{left:270px}
  .seal-band{position:absolute;left:0;right:0;top:22px;height:10px;background:var(--accent)}
  .zip-line{position:absolute;left:0;right:0;top:50px;height:1px;background:rgba(0,0,0,.08)}

  /* back */
  .brand-mini{position:absolute;top:64px;left:0;right:0;text-align:center;font-family:"Alfa Slab One",serif;line-height:1}
  .brand-mini .cuts{font-family:"Oswald",sans-serif;font-size:5px;letter-spacing:2px;display:block;margin-bottom:3px}
  .brand-mini .name{font-size:13px;display:block}
  .brand-mini .sub{font-size:8px;display:block;margin-top:2px}
  .story{position:absolute;top:120px;left:34px;right:26px;font-size:5.5px;font-weight:700;text-align:center;line-height:1.35;text-transform:uppercase}
  .ingredients{position:absolute;top:158px;left:34px;width:110px;font-size:5px;line-height:1.4}
  .ingredients p{margin-bottom:5px}
  .nutrition{position:absolute;top:156px;left:150px;width:82px;border:1px solid var(--ink);background:#fff;padding:3px;font-size:4.5px}
  .nutrition h4{font-family:"Oswald",sans-serif;font-size:8px;font-weight:500;border-bottom:1px solid var(--ink);margin-bottom:2px}
  .nutrition table{width:100%;border-collapse:collapse}
  .nutrition td{border-bottom:.5px solid #999;padding:.5px 0}
  .nutrition td+td{text-align:right}
  .origin-label{position:absolute;top:254px;left:34px;font-size:4px;font-weight:700}
  .origin-badge{position:absolute;top:262px;left:34px;width:48px;height:14px;background:#2e7d32;border-radius:2px}
  .jerky-window{position:absolute;left:0;right:0;top:288px;height:40px;border-top:4px solid #111;border-bottom:4px solid #111;
    background:linear-gradient(100deg,var(--jerky-dark),var(--jerky) 30%,#8e4a2a 55%,var(--jerky-dark) 80%,var(--jerky))}

  /* front */
  .brand{position:absolute;top:58px;left:0;right:0;text-align:center;font-family:"Alfa Slab One",serif;line-height:1}
  .brand .cuts{font-family:"Oswald",sans-serif;font-size:8px;letter-spacing:3px;display:block;margin-bottom:9px}
  .brand .dot{display:inline-block;width:6px;height:6px;border-radius:50%;background:var(--ink);vertical-align:middle;margin-right:5px}
  .brand .name{font-size:26px;display:block;letter-spacing:.5px}
  .brand .sub{font-size:14px;display:block;margin-top:6px;letter-spacing:2px}
  .flavour-art{position:absolute;top:150px;right:12px;width:66px;height:52px;border-radius:10px}
  .chilli .flavour-art{background:linear-gradient(135deg,#c9261f,#8b1510)}
  .original .flavour-art{background:linear-gradient(135deg,#8c8a78,#5a6640)}
  .pepper .flavour-art{background:linear-gradient(135deg,#6b4630,#2a1a12)}
  .mongolian .flavour-art{background:linear-gradient(135deg,#c9473b,#7a1f18)}
  .farm-scene{position:absolute;top:262px;left:16px;width:120px;height:44px;border-radius:6px;
    background:linear-gradient(180deg,rgba(180,180,180,0),rgba(170,170,170,.35))}
  .tag-string{position:absolute;top:180px;left:18px;width:150px;height:80px}
  .flavour-tag{position:absolute;top:210px;left:108px;width:146px;height:84px;background:linear-gradient(160deg,var(--kraft),var(--kraft-dark));
    transform:rotate(20deg);border-radius:4px;padding:9px 6px 0 22px;text-align:center;box-shadow:0 2px 4px rgba(0,0,0,.25);
    font-family:"Alfa Slab One",serif;color:#4a3420;line-height:1.05}
  .flavour-tag::before{content:"";position:absolute;left:7px;top:36px;width:10px;height:10px;border-radius:50%;background:var(--pouch-light);border:2px solid #5b4127}
  .flavour-tag .small{font-size:7px;display:block}
  .flavour-tag .flavour{font-size:20px;color:var(--accent);display:block;margin:2px 0}
  .flavour-tag .flavour.long{font-size:15px}
  .flavour-tag .flavour.two-line{font-size:14px;margin:1px 0}
  .claims{position:absolute;top:322px;left:16px;right:12px;display:flex;align-items:center;gap:5px;color:var(--accent);font-family:"Oswald",sans-serif;font-weight:700}
  .claim{display:flex;align-items:center;gap:2px;padding-right:5px;border-right:1px solid var(--accent)}
  .claim:last-child{border:none}
  .claim .big{font-size:17px;line-height:1}
  .claim .fine{font-family:"Roboto Condensed",sans-serif;font-size:3.6px;line-height:1.2;font-weight:700;text-transform:uppercase}
  .claim .gf{font-size:8px;line-height:1}
</style>
</head>
<body>
<main class="range">

  <section class="flavour-pair chilli">
    <article class="pouch back">
      <div class="seal-band"></div><div class="zip-line"></div>
      <div class="brand-mini"><span class="cuts">PREMIUM CUTS</span><span class="name">BRINDLE<br>HOLLOW</span><span class="sub">JERKY</span></div>
      <p class="story">Made in the sunshine state with the finest cuts of Australian beef, handcrafted and seasoned in small batches. We recommend sharing in the company of great friends over your favourite craft beer – but that's just us!</p>
      <div class="ingredients"><p><b>INGREDIENTS:</b> Australian beef, sugar, spices, salt, soy sauce, wheat flour, potassium sorbate, monosodium glutamate.</p><p>Allergens: contains soy and wheat flour.</p><p>Please store in a dry airtight container after opening.</p><p>Packed in Australia</p></div>
      <div class="nutrition"><h4>Nutrition Facts</h4><table><tr><td>Energy</td><td>405kJ</td></tr><tr><td>Protein</td><td>12.5g</td></tr><tr><td>Fat</td><td>2.2g</td></tr><tr><td>Carbohydrate</td><td>6.7g</td></tr><tr><td>Sugar</td><td>5.9g</td></tr><tr><td>Sodium</td><td>270mg</td></tr></table></div>
      <span class="origin-label">AUSTRALIAN MADE AND OWNED</span>
      <div class="origin-badge"></div>
      <div class="jerky-window" role="img" aria-label="Photograph of beef jerky strips"></div>
    </article>
    <article class="pouch front">
      <div class="seal-band"></div><div class="zip-line"></div>
      <div class="brand"><span class="cuts"><span class="dot"></span>PREMIUM CUTS</span><span class="name">BRINDLE<br>HOLLOW</span><span class="sub">JERKY</span></div>
      <div class="flavour-art" role="img" aria-label="Illustration of red chillies and chilli flakes"></div>
      <div class="farm-scene" role="img" aria-label="Faint sketch of a country farm landscape"></div>
      <svg class="tag-string" viewBox="0 0 150 80"><path d="M8 10 C40 20,70 40,112 58" fill="none" stroke="#8a6a44" stroke-width="1.2"/><path d="M8 10 C30 40,80 60,112 58" fill="none" stroke="#8a6a44" stroke-width="1.2"/><circle cx="8" cy="10" r="6" fill="#c8321f"/></svg>
      <div class="flavour-tag"><span class="small">WHOLE INGREDIENTS</span><span class="flavour">CHILLI</span><span class="small">MADE FROM 100%<br>AUSTRALIAN BEEF</span></div>
      <div class="claims"><div class="claim"><span class="big">NO</span><span class="fine">added<br>preservatives<br>or colours</span></div><div class="claim"><span class="big">11G</span><span class="fine">protein<br>per serve</span></div><div class="claim"><span class="big">60G</span><span class="fine">net<br>weight</span></div><div class="claim"><span class="gf">GLUTEN<br>FREE</span></div></div>
    </article>
  </section>

  <section class="flavour-pair original">
    <article class="pouch back">
      <div class="seal-band"></div><div class="zip-line"></div>
      <div class="brand-mini"><span class="cuts">PREMIUM CUTS</span><span class="name">BRINDLE<br>HOLLOW</span><span class="sub">JERKY</span></div>
      <p class="story">Made in the sunshine state with the finest cuts of Australian beef, handcrafted and seasoned in small batches. We recommend sharing in the company of great friends over your favourite craft beer – but that's just us!</p>
      <div class="ingredients"><p><b>INGREDIENTS:</b> Australian beef, sugar, spices, salt, soy sauce, wheat flour, potassium sorbate, monosodium glutamate.</p><p>Allergens: contains soy and wheat flour.</p><p>Please store in a dry airtight container after opening.</p><p>Packed in Australia</p></div>
      <div class="nutrition"><h4>Nutrition Facts</h4><table><tr><td>Energy</td><td>405kJ</td></tr><tr><td>Protein</td><td>12.5g</td></tr><tr><td>Fat</td><td>2.2g</td></tr><tr><td>Carbohydrate</td><td>6.7g</td></tr><tr><td>Sugar</td><td>5.9g</td></tr><tr><td>Sodium</td><td>270mg</td></tr></table></div>
      <span class="origin-label">AUSTRALIAN MADE AND OWNED</span>
      <div class="origin-badge"></div>
      <div class="jerky-window" role="img" aria-label="Photograph of beef jerky strips"></div>
    </article>
    <article class="pouch front">
      <div class="seal-band"></div><div class="zip-line"></div>
      <div class="brand"><span class="cuts"><span class="dot"></span>PREMIUM CUTS</span><span class="name">BRINDLE<br>HOLLOW</span><span class="sub">JERKY</span></div>
      <div class="flavour-art" role="img" aria-label="Illustration of herbs, garlic, onion and mortar with pestle"></div>
      <div class="farm-scene" role="img" aria-label="Faint sketch of a country farm landscape"></div>
      <svg class="tag-string" viewBox="0 0 150 80"><path d="M8 10 C40 20,70 40,112 58" fill="none" stroke="#8a6a44" stroke-width="1.2"/><path d="M8 10 C30 40,80 60,112 58" fill="none" stroke="#8a6a44" stroke-width="1.2"/><circle cx="8" cy="10" r="6" fill="#c8321f"/></svg>
      <div class="flavour-tag"><span class="small">WHOLE INGREDIENTS</span><span class="flavour long">ORIGINAL</span><span class="small">MADE FROM 100%<br>AUSTRALIAN BEEF</span></div>
      <div class="claims"><div class="claim"><span class="big">NO</span><span class="fine">added<br>preservatives<br>or colours</span></div><div class="claim"><span class="big">11G</span><span class="fine">protein<br>per serve</span></div><div class="claim"><span class="big">60G</span><span class="fine">net<br>weight</span></div><div class="claim"><span class="gf">GLUTEN<br>FREE</span></div></div>
    </article>
  </section>

  <section class="flavour-pair pepper">
    <article class="pouch back">
      <div class="seal-band"></div><div class="zip-line"></div>
      <div class="brand-mini"><span class="cuts">PREMIUM CUTS</span><span class="name">BRINDLE<br>HOLLOW</span><span class="sub">JERKY</span></div>
      <p class="story">Made in the sunshine state with the finest cuts of Australian beef, handcrafted and seasoned in small batches. We recommend sharing in the company of great friends over your favourite craft beer – but that's just us!</p>
      <div class="ingredients"><p><b>INGREDIENTS:</b> Australian beef, sugar, spices, salt, soy sauce, wheat flour, potassium sorbate, monosodium glutamate.</p><p>Allergens: contains soy and wheat flour.</p><p>Please store in a dry airtight container after opening.</p><p>Packed in Australia</p></div>
      <div class="nutrition"><h4>Nutrition Facts</h4><table><tr><td>Energy</td><td>405kJ</td></tr><tr><td>Protein</td><td>12.5g</td></tr><tr><td>Fat</td><td>2.2g</td></tr><tr><td>Carbohydrate</td><td>6.7g</td></tr><tr><td>Sugar</td><td>5.9g</td></tr><tr><td>Sodium</td><td>270mg</td></tr></table></div>
      <span class="origin-label">AUSTRALIAN MADE AND OWNED</span>
      <div class="origin-badge"></div>
      <div class="jerky-window" role="img" aria-label="Photograph of beef jerky strips"></div>
    </article>
    <article class="pouch front">
      <div class="seal-band"></div><div class="zip-line"></div>
      <div class="brand"><span class="cuts"><span class="dot"></span>PREMIUM CUTS</span><span class="name">BRINDLE<br>HOLLOW</span><span class="sub">JERKY</span></div>
      <div class="flavour-art" role="img" aria-label="Illustration of smoking wood logs and a scoop of peppercorns"></div>
      <div class="farm-scene" role="img" aria-label="Faint sketch of a country farm landscape"></div>
      <svg class="tag-string" viewBox="0 0 150 80"><path d="M8 10 C40 20,70 40,112 58" fill="none" stroke="#8a6a44" stroke-width="1.2"/><path d="M8 10 C30 40,80 60,112 58" fill="none" stroke="#8a6a44" stroke-width="1.2"/><circle cx="8" cy="10" r="6" fill="#c8321f"/></svg>
      <div class="flavour-tag"><span class="small">WHOLE INGREDIENTS</span><span class="flavour two-line">SMOKED<br>PEPPER</span><span class="small">MADE FROM 100%<br>AUSTRALIAN BEEF</span></div>
      <div class="claims"><div class="claim"><span class="big">NO</span><span class="fine">added<br>preservatives<br>or colours</span></div><div class="claim"><span class="big">11G</span><span class="fine">protein<br>per serve</span></div><div class="claim"><span class="big">60G</span><span class="fine">net<br>weight</span></div><div class="claim"><span class="gf">GLUTEN<br>FREE</span></div></div>
    </article>
  </section>

  <section class="flavour-pair mongolian">
    <article class="pouch back">
      <div class="seal-band"></div><div class="zip-line"></div>
      <div class="brand-mini"><span class="cuts">PREMIUM CUTS</span><span class="name">BRINDLE<br>HOLLOW</span><span class="sub">JERKY</span></div>
      <p class="story">Made in the sunshine state with the finest cuts of Australian beef, handcrafted and seasoned in small batches. We recommend sharing in the company of great friends over your favourite craft beer – but that's just us!</p>
      <div class="ingredients"><p><b>INGREDIENTS:</b> Australian beef, sugar, spices, salt, soy sauce, wheat flour, potassium sorbate, monosodium glutamate.</p><p>Allergens: contains soy and wheat flour.</p><p>Please store in a dry airtight container after opening.</p><p>Packed in Australia</p></div>
      <div class="nutrition"><h4>Nutrition Facts</h4><table><tr><td>Energy</td><td>405kJ</td></tr><tr><td>Protein</td><td>12.5g</td></tr><tr><td>Fat</td><td>2.2g</td></tr><tr><td>Carbohydrate</td><td>6.7g</td></tr><tr><td>Sugar</td><td>5.9g</td></tr><tr><td>Sodium</td><td>270mg</td></tr></table></div>
      <span class="origin-label">AUSTRALIAN MADE AND OWNED</span>
      <div class="origin-badge"></div>
      <div class="jerky-window" role="img" aria-label="Photograph of beef jerky strips"></div>
    </article>
    <article class="pouch front">
      <div class="seal-band"></div><div class="zip-line"></div>
      <div class="brand"><span class="cuts"><span class="dot"></span>PREMIUM CUTS</span><span class="name">BRINDLE<br>HOLLOW</span><span class="sub">JERKY</span></div>
      <div class="flavour-art" role="img" aria-label="Illustration of garlic, chillies and a bowl of sauce"></div>
      <div class="farm-scene" role="img" aria-label="Faint sketch of a country farm landscape"></div>
      <svg class="tag-string" viewBox="0 0 150 80"><path d="M8 10 C40 20,70 40,112 58" fill="none" stroke="#8a6a44" stroke-width="1.2"/><path d="M8 10 C30 40,80 60,112 58" fill="none" stroke="#8a6a44" stroke-width="1.2"/><circle cx="8" cy="10" r="6" fill="#c8321f"/></svg>
      <div class="flavour-tag"><span class="small">WHOLE INGREDIENTS</span><span class="flavour long">MONGOLIAN</span><span class="small">MADE FROM 100%<br>AUSTRALIAN BEEF</span></div>
      <div class="claims"><div class="claim"><span class="big">NO</span><span class="fine">added<br>preservatives<br>or colours</span></div><div class="claim"><span class="big">11G</span><span class="fine">protein<br>per serve</span></div><div class="claim"><span class="big">60G</span><span class="fine">net<br>weight</span></div><div class="claim"><span class="gf">GLUTEN<br>FREE</span></div></div>
    </article>
  </section>

</main>
</body>
</html>
```